New Architectural Firm Business Cards

New Business card to compliment previous pixel forum logo (attached). Please design a business card that is simple, modern, creative....please do not use "symbols", simply the logo and associated graphics/text. The front should contain name/address/phone/email/web address (with graphics).....back should be 100% graphic design using the logo somehow. Hoping for a two color (black and yellow) design. full bleed design, no borders

Target Market(s)

Commercial Architecture Clients

Industry/Entity Type

Architecture

Contact Information for Business Card

Please design a business card that is simple, modern, creative....please do not use "symbols", simply the logo and associated graphics/text. The front should contain name/address/phone/email/web address (with graphics).....back should be 100% graphic design using the logo somehow

Font styles to use
Sans Serif

Colors
FFF300
FFF600
FEFA6F
FFFEC7
FFFEE8

Requirements
Must have
• Clean, Modern Design
Should not have
• Stock images or "icons"

```html
<!DOCTYPE html>
<html lang="en">
<head>
<meta charset="utf-8">
<title>Pixel Forum Business Card</title>
<link href="https://fonts.googleapis.com/css2?family=Montserrat:wght@400;500;600&display=swap" rel="stylesheet">
<style>
  :root {
    --stage: #d9d6d1;
    --cream: #fbf9ea;
    --yellow: #f2c414;
    --charcoal: #3b393a;
    --charcoal-dark: #2a2829;
    --ink: #3a3536;
    --white: #f1f1f1;
  }
  * { margin: 0; padding: 0; box-sizing: border-box; }
  html, body {
    width: 1200px; height: 900px; overflow: hidden;
    background: var(--stage);
    font-family: "Montserrat", sans-serif;
  }
  .canvas {
    width: 1200px; height: 900px;
    display: flex; flex-direction: column; align-items: center; justify-content: center; gap: 40px;
  }
  .card {
    position: relative; width: 700px; height: 400px; overflow: hidden;
    box-shadow: 0 10px 28px rgba(0,0,0,.22);
  }
  .card-shape { position: absolute; inset: 0; }

  /* front */
  .card-front { background: var(--yellow); }
  .front-brand {
    position: absolute; left: 60px; top: 215px;
    display: flex; align-items: center; gap: 12px;
  }
  .brand-mark { width: 22px; height: 22px; background: var(--yellow); flex: none; }
  .brand-name {
    font-size: 34px; font-weight: 600; color: var(--yellow); letter-spacing: -.5px;
    line-height: 1; white-space: nowrap;
  }
  .contact {
    position: absolute; right: 44px; top: 48px; text-align: right; color: var(--ink);
  }
  .contact-name { font-size: 24px; font-weight: 500; letter-spacing: 1px; }
  .contact-role { font-size: 10px; letter-spacing: 2px; margin-bottom: 26px; }
  .contact-line { font-size: 13px; line-height: 1.55; }
  .contact-gap { height: 12px; }
  .web-band {
    position: absolute; right: 0; top: 292px; width: 290px; height: 46px;
    background: var(--charcoal);
    display: flex; align-items: center; justify-content: flex-end; padding-right: 30px;
  }
  .web-address { color: var(--white); font-size: 22px; font-weight: 500; }

  /* back */
  .card-back {
    background: radial-gradient(ellipse at 35% 30%, #4a4748 0%, var(--charcoal) 55%, var(--charcoal-dark) 100%);
  }
  .back-brand {
    position: absolute; left: 110px; top: 170px;
    display: flex; align-items: center; gap: 16px;
  }
  .back-brand .brand-mark { width: 30px; height: 30px; }
  .back-brand .brand-name { font-size: 52px; }
  .back-bar {
    position: absolute; left: 520px; right: 0; top: 170px; height: 34px; background: var(--white);
  }
</style>
</head>
<body>
<main class="canvas">
  <section class="card card-front" aria-label="Card front">
    <svg class="card-shape" viewBox="0 0 700 400" aria-hidden="true">
      <path d="M0 0 H250 C350 0 375 130 385 400 H0 Z" fill="var(--cream)"/>
    </svg>
    <div class="front-brand">
      <span class="brand-mark"></span>
      <span class="brand-name">Pixel Forum</span>
    </div>
    <div class="contact">
      <p class="contact-name">LENA HART</p>
      <p class="contact-role">ARCHITECT</p>
      <p class="contact-line">Harbor Lane 210</p>
      <p class="contact-line">Portland, Oregon</p>
      <div class="contact-gap"></div>
      <p class="contact-line">(000) 555-0142</p>
      <p class="contact-line">lena@pixelforum.com</p>
    </div>
    <div class="web-band"><span class="web-address">pixelforum.com</span></div>
  </section>

  <section class="card card-back" aria-label="Card back">
    <div class="back-bar"></div>
    <div class="back-brand">
      <span class="brand-mark"></span>
      <span class="brand-name">Pixel Forum</span>
    </div>
  </section>
</main>
</body>
</html>
```